Building Referrer Relationships Booklet

4 page A4 booklet to give to potential professional referrers to establish a collaborative relationship.Needs to be bright, vibrant, colourful, friendly, inviting, in keeping with The Wren Clinic colours.
Want to provide potential referrer partners a great reason to choose to collaborate with us. They need to know who we are, what makes us different/appealing, and who we are looking for to connect with.
The final product should communicate high performance and connectedness.

Target Market(s)

professional medical allied health and fitness practitioners

Industry/Entity Type

Health

Requirements
Must have
• energetic, vibrant, engaging, inviting, images

```html
<!DOCTYPE html>
<html lang="en">
<head>
<meta charset="utf-8">
<title>The Wren Clinic – Referral Partnerships Booklet</title>
<link href="https://fonts.googleapis.com/css2?family=Montserrat:wght@400;500;600;700;800&family=Open+Sans:wght@400;600&display=swap" rel="stylesheet">
<style>
:root{
  --bg:#e4e5e8;
  --paper:#ffffff;
  --blue:#2f8be6;
  --blue-light:#5aa7f0;
  --navy:#0d4f9f;
  --navy-dark:#0a3f82;
  --orange:#f0891d;
  --green:#2e8a34;
  --ink:#2b2f36;
  --muted:#6b7079;
  --photo-a:#5f7f5a;
  --photo-b:#6c93b8;
}
*{box-sizing:border-box;margin:0;padding:0}
html,body{width:1200px;height:4000px;overflow:hidden;background:var(--bg)}
body{font-family:"Montserrat",sans-serif;color:var(--ink)}
.booklet{position:relative;width:1200px;height:4000px}
.page{position:absolute;left:260px;width:680px;height:962px;background:var(--paper);overflow:hidden;box-shadow:0 2px 10px rgba(0,0,0,.08)}
.page--cover{top:30px}
.page--about{top:1022px}
.page--method{top:2014px}
.page--partners{top:3006px}

/* brand */
.brand{display:flex;align-items:center;gap:10px}
.brand__mark{width:34px;height:34px;background:var(--blue)}
.brand__name{font-weight:600;font-size:18px;line-height:1.05;color:var(--navy)}

/* cover */
.cover__brand{position:absolute;top:34px;right:50px}
.cover__photo{position:absolute;left:50px;right:0;top:120px;height:530px;background:linear-gradient(180deg,#7fa3c8 0%,var(--photo-b) 30%,var(--photo-a) 62%,#4e8fbf 100%)}
.cover__band{position:absolute;left:50px;right:0;top:588px;height:108px;background:linear-gradient(90deg,var(--blue) 0%,var(--blue-light) 100%);text-align:center;color:#fff;padding-top:24px}
.cover__title{font-weight:800;font-size:34px;letter-spacing:1px}
.cover__tag{font-weight:500;font-size:12px;letter-spacing:2px;margin-top:6px;opacity:.9}
.cover__lead{position:absolute;left:50px;right:0;top:760px;text-align:center;font-weight:700;font-size:12.5px;line-height:2;letter-spacing:.5px}
.cover__url{position:absolute;left:50px;right:0;top:850px;text-align:center;font-weight:700;font-size:14px;letter-spacing:1.5px}

/* about page */
.about__panel{position:absolute;left:0;top:0;width:440px;height:560px;background:linear-gradient(180deg,var(--blue) 0%,#4f9fee 100%);padding:34px 30px;color:#fff}
.section-title{font-weight:700;font-size:17px;letter-spacing:1px}
.values{list-style:none;margin-top:20px}
.values li{position:relative;padding-left:24px;margin-bottom:17px}
.values li::before{content:"";position:absolute;left:0;top:2px;width:12px;height:12px;border-radius:50%;border:3px solid var(--orange);background:#fff}
.values h4{font-size:13px;font-weight:700;color:var(--orange);letter-spacing:.5px}
.values p{font-family:"Open Sans",sans-serif;font-size:10.5px;line-height:1.45;margin-top:3px}
.team{position:absolute;left:460px;top:34px;width:200px}
.team .section-title{color:var(--blue)}
.team__list{list-style:none;margin-top:14px}
.member{display:flex;gap:8px;margin-bottom:11px}
.member__photo{flex:none;width:44px;height:52px;background:linear-gradient(180deg,#cfd5dc,#8e99a6)}
.member__name{font-size:10px;font-weight:700;margin-top:4px}
.member__role{font-family:"Open Sans",sans-serif;font-size:8.5px;color:var(--muted);line-height:1.35}
.about__statement{position:absolute;left:30px;right:30px;top:590px}
.statement{font-weight:800;font-size:19px;line-height:1.3;color:var(--orange);letter-spacing:.5px}
.top3{font-weight:700;font-size:13px;color:var(--blue);margin-top:20px;line-height:1.4}
.reasons{list-style:none;margin-top:16px}
.reasons li{margin-bottom:14px}
.reasons h5{font-size:12.5px;font-weight:700;color:var(--orange)}
.reasons p{font-size:10px;color:var(--muted);margin-top:3px;letter-spacing:.3px}

/* method page */
.method{padding:34px 36px}
.method .section-title{color:var(--blue)}
.method__intro{font-family:"Open Sans",sans-serif;font-size:11px;line-height:1.5;margin-top:10px}
.method__photo{height:190px;margin:20px 40px 0 40px;background:linear-gradient(90deg,#c9d6e4 0%,#e9e2dc 55%,#b8c8da 100%)}
.method__cols{display:grid;grid-template-columns:1fr 1fr;gap:26px;margin-top:26px}
.pillar{font-weight:700;font-size:13px;color:var(--orange);letter-spacing:.5px}
.step{margin-top:16px}
.step h4{font-size:12.5px;font-weight:700}
.step .sub{font-family:"Open Sans",sans-serif;font-size:11px;color:var(--ink)}
.ticks{list-style:none;margin-top:5px}
.ticks li{position:relative;padding-left:16px;font-family:"Open Sans",sans-serif;font-size:10.5px;line-height:1.6}
.ticks li::before{content:"✓";position:absolute;left:2px;top:0;color:var(--blue);font-weight:700}
.repeat{margin-top:20px}
.repeat__lists{display:grid;grid-template-columns:1fr 1fr;gap:26px}

/* partners page */
.partners__panel{position:absolute;left:0;top:0;width:100%;height:790px;background:linear-gradient(180deg,var(--navy) 0%,var(--navy-dark) 100%);padding:36px 40px;color:#fff}
.partners__panel .section-title{font-size:18px}
.roles{list-style:none;margin-top:22px}
.role{margin-bottom:15px;padding-left:26px;position:relative}
.role svg{position:absolute;left:0;top:0}
.role h4{font-size:12.5px;font-weight:700;letter-spacing:.5px}
.role .ticks li{color:#fff;font-size:10px}
.role .ticks li::before{color:#9fd0ff}
.contact{position:absolute;left:40px;right:40px;top:812px}
.contact__call{font-weight:800;font-size:30px;color:var(--green);letter-spacing:1px}
.contact__line{display:flex;align-items:center;gap:7px;font-size:12px;margin-top:7px;color:var(--ink)}
.affiliates{position:absolute;right:40px;bottom:40px;display:flex;gap:10px}
.affiliates span{width:54px;height:26px;background:#d3d7dd;border-radius:3px}
</style>
</head>
<body>
<main class="booklet">

  <section class="page page--cover">
    <div class="brand cover__brand">
      <span class="brand__mark"></span>
      <span class="brand__name">Coastal Podiatry Guild</span>
    </div>
    <div class="cover__photo" role="img" aria-label="Photo of a group of athletes in running kits standing together on a stadium track"></div>
    <div class="cover__band">
      <h1 class="cover__title">REFERRAL PARTNERSHIPS</h1>
      <p class="cover__tag">BECAUSE TOGETHER WE ACHIEVE MORE</p>
    </div>
    <p class="cover__lead">WE ARE HERE TO HELP OUR CLIENTS GET BACK ON THEIR FEET<br>LET'S COMBINE OUR SKILLSETS SO WE CAN ACHIEVE EVEN BETTER RESULTS.</p>
    <p class="cover__url">www.wrenreferrals.com</p>
  </section>

  <section class="page page--about">
    <div class="about__panel">
      <h2 class="section-title">ABOUT US:</h2>
      <ul class="values">
        <li><h4>COURAGE</h4><p>Courage gives us the strength and confidence to take risks and embrace challenges.</p></li>
        <li><h4>INSPIRATION</h4><p>Inspiration is our energy, our fuel for success. Our team inspire clients to achieve great outcomes.</p></li>
        <li><h4>FUN</h4><p>Fun generates happiness, and we never lose sight of the joy that movement brings.</p></li>
        <li><h4>CREATION</h4><p>Creativity sets us apart as innovative leaders in foot and posture care.</p></li>
        <li><h4>WORK</h4><p>Work ethic drives our team to go the extra mile and create lasting results for every client we meet.</p></li>
        <li><h4>TEAM</h4><p>Teamwork is central to performance; we grow by combining strengths and sharing knowledge.</p></li>
      </ul>
    </div>
    <div class="team">
      <h2 class="section-title">OUR TEAM</h2>
      <ul class="team__list">
        <li class="member"><div class="member__photo" role="img" aria-label="Portrait of team member"></div><div><p class="member__role">Principal Podiatrist</p><p class="member__name">DR MARCUS ELLORY</p></div></li>
        <li class="member"><div class="member__photo" role="img" aria-label="Portrait of team member"></div><div><p class="member__role">Sports Podiatrist</p><p class="member__name">DR TESSA LANGFORD</p></div></li>
        <li class="member"><div class="member__photo" role="img" aria-label="Portrait of team member"></div><div><p class="member__role">Biomechanics Podiatrist</p><p class="member__name">DR NADIA FARROW</p></div></li>
        <li class="member"><div class="member__photo" role="img" aria-label="Portrait of team member"></div><div><p class="member__role">Podiatrist</p><p class="member__name">DR FELIX HARMON</p></div></li>
        <li class="member"><div class="member__photo" role="img" aria-label="Portrait of team member"></div><div><p class="member__role">Practice Manager</p><p class="member__name">OWEN PRITCHARD</p></div></li>
        <li class="member"><div class="member__photo" role="img" aria-label="Portrait of team member"></div><div><p class="member__role">Client Care Lead</p><p class="member__name">CARLA BENNING</p></div></li>
      </ul>
    </div>
    <div class="about__statement">
      <p class="statement">AT THE WREN CLINIC, WE ARE PASSIONATE ABOUT BUILDING STRONG POSTURAL FOUNDATIONS, FROM THE FEET UP</p>
      <p class="top3">THE TOP 3 THINGS OUR CLIENTS LOVE ABOUT US<br>(AND HOPEFULLY YOURS WILL TOO):</p>
      <ol class="reasons">
        <li><h5>1.POSITIVE ENERGY, ENTHUSIASM AND OUTCOMES</h5><p>NPS AVERAGE SCORE 9 OUT OF 10</p></li>
        <li><h5>2.TRUSTED LEADER IN THE PRACTICE OF PODIATRIC MEDICINE</h5><p>ESTABLISHED 1998, ELITE EXPERIENCE, LATEST HIGH-TECH EQUIPMENT</p></li>
        <li><h5>3.FOCUS IS ON STRONG FEET, NOT JUST ORTHOTICS!</h5><p>BAREFOOT TRAINING METHOD, FASCIAL LINES METHOD, FOOT MANUAL THERAPIES</p></li>
      </ol>
    </div>
  </section>

  <section class="page page--method method">
    <h2 class="section-title">THE WREN CLINIC WAY</h2>
    <p class="method__intro">Our pathway to strengthen postural foundations, to create lasting changes for freedom of movement and ultimately keep us going well beyond what we thought was possible (updated to research and tech changes).</p>
    <div class="method__photo" role="img" aria-label="Photo of a practitioner's gloved hands treating a client's bare foot"></div>
    <div class="method__cols">
      <div>
        <h3 class="pillar">FIX YOUR FEET</h3>
        <div class="step"><h4>1.FIX THE PAIN</h4>
          <ul class="ticks"><li>Provide analgesia</li><li>Reduce inflammation</li><li>Correct alignment and load</li><li>Ingrown toenail and wound care</li><li>Surgery</li></ul></div>
        <div class="step"><h4>2.PROTECT THE FEET</h4><p class="sub">(reduce damage, optimise stability, promote healing)</p>
          <ul class="ticks"><li>Reduce tissue damage</li><li>Optimise foot posture</li><li>Activate muscles to improve balance</li><li>Promote tissue repair</li></ul></div>
        <div class="step"><h4>3.STRENGTHEN THE FEET</h4><p class="sub">(increase strength and resilience)</p>
          <ul class="ticks"><li>Strengthen intrinsics</li><li>Connect foot strength to core</li><li>Stimulate neuromuscular strength</li></ul></div>
      </div>
      <div>
        <h3 class="pillar">BIOHACK YOUR BODY</h3>
        <div class="step"><h4>4.PROTECT THE WHOLE BODY</h4><p class="sub">(stability)</p>
          <ul class="ticks"><li>Optimise postural alignment</li><li>Activate neuromuscular reflexes</li><li>Customised corrective exercise</li><li>Improve cellular regeneration</li><li>Optimise healthy mind</li></ul></div>
        <div class="step"><h4>5.STRENGTHEN THE WHOLE BODY</h4><p class="sub">(strength, elasticity)</p>
          <ul class="ticks"><li>Strengthen the deep core</li><li>Increase fascial elasticity</li><li>Increase functional strength</li><li>Tailored nutrition for performance</li><li>Improve psychological resilience</li></ul></div>
      </div>
    </div>
    <div class="step repeat"><h4>6.REPEAT CONSISTENTLY</h4>
      <div class="repeat__lists">
        <ul class="ticks"><li>The Elite Athlete Experience</li><li>National Sports Academy</li><li>National Rugby Squad</li><li>Summer Games</li></ul>
        <ul class="ticks"><li>Harbour City Triathlon Championships</li><li>Regional Games</li><li>International Tennis Cup</li></ul>
      </div>
    </div>
  </section>

  <section class="page page--partners">
    <div class="partners__panel">
      <h2 class="section-title">REFERRAL PARTNERS REQUIRED:</h2>
      <ul class="roles">
        <li class="role"><svg width="16" height="16" viewBox="0 0 16 16"><circle cx="8" cy="8" r="7" fill="none" stroke="#fff" stroke-width="1.6"/><path d="M4.5 8.2l2.3 2.3 4.7-4.9" fill="none" stroke="#fff" stroke-width="1.6"/></svg><h4>MASSAGE THERAPISTS</h4><ul class="ticks"><li>Deep tissue and remedial massage</li><li>Therapeutic massage</li></ul></li>
        <li class="role"><svg width="16" height="16" viewBox="0 0 16 16"><circle cx="8" cy="8" r="7" fill="none" stroke="#fff" stroke-width="1.6"/><path d="M4.5 8.2l2.3 2.3 4.7-4.9" fill="none" stroke="#fff" stroke-width="1.6"/></svg><h4>FASCIAL THERAPISTS</h4><ul class="ticks"><li>Releasing fascial restriction to reset the alignment of the whole body</li></ul></li>
        <li class="role"><svg width="16" height="16" viewBox="0 0 16 16"><circle cx="8" cy="8" r="7" fill="none" stroke="#fff" stroke-width="1.6"/><path d="M4.5 8.2l2.3 2.3 4.7-4.9" fill="none" stroke="#fff" stroke-width="1.6"/></svg><h4>PHYSIOTHERAPISTS</h4><ul class="ticks"><li>Rehab, protect and strengthen both lower limb and upper limb</li></ul></li>
        <li class="role"><svg width="16" height="16" viewBox="0 0 16 16"><circle cx="8" cy="8" r="7" fill="none" stroke="#fff" stroke-width="1.6"/><path d="M4.5 8.2l2.3 2.3 4.7-4.9" fill="none" stroke="#fff" stroke-width="1.6"/></svg><h4>GP, SPORTS PHYSICIANS</h4><ul class="ticks"><li>General health, diagnostics, treatment support, prescription medications</li><li>Specialist referrals</li></ul></li>
        <li class="role"><svg width="16" height="16" viewBox="0 0 16 16"><circle cx="8" cy="8" r="7" fill="none" stroke="#fff" stroke-width="1.6"/><path d="M4.5 8.2l2.3 2.3 4.7-4.9" fill="none" stroke="#fff" stroke-width="1.6"/></svg><h4>OSTEOPATHS AND CHIROPRACTORS</h4><ul class="ticks"><li>Mobilisation and manipulative therapy for the spinal column and limbs</li></ul></li>
        <li class="role"><svg width="16" height="16" viewBox="0 0 16 16"><circle cx="8" cy="8" r="7" fill="none" stroke="#fff" stroke-width="1.6"/><path d="M4.5 8.2l2.3 2.3 4.7-4.9" fill="none" stroke="#fff" stroke-width="1.6"/></svg><h4>DIETICIAN AND NUTRITIONISTS</h4><ul class="ticks"><li>Ideal fuel for bone density, lean mass, fat mass</li><li>Optimising gut health and nutrition – you are what you eat!</li></ul></li>
        <li class="role"><svg width="16" height="16" viewBox="0 0 16 16"><circle cx="8" cy="8" r="7" fill="none" stroke="#fff" stroke-width="1.6"/><path d="M4.5 8.2l2.3 2.3 4.7-4.9" fill="none" stroke="#fff" stroke-width="1.6"/></svg><h4>PSYCHOLOGISTS/PSYCHIATRISTS</h4><ul class="ticks"><li>Sometimes our physical body cannot get better until we optimise a healthy mind</li></ul></li>
        <li class="role"><svg width="16" height="16" viewBox="0 0 16 16"><circle cx="8" cy="8" r="7" fill="none" stroke="#fff" stroke-width="1.6"/><path d="M4.5 8.2l2.3 2.3 4.7-4.9" fill="none" stroke="#fff" stroke-width="1.6"/></svg><h4>PERSONAL TRAINERS, PILATES AND YOGA INSTRUCTORS</h4><ul class="ticks"><li>Create awesome body strength, flexibility and resilience</li></ul></li>
        <li class="role"><svg width="16" height="16" viewBox="0 0 16 16"><circle cx="8" cy="8" r="7" fill="none" stroke="#fff" stroke-width="1.6"/><path d="M4.5 8.2l2.3 2.3 4.7-4.9" fill="none" stroke="#fff" stroke-width="1.6"/></svg><h4>SURGEONS</h4><ul class="ticks"><li>When conservative methods are ineffective, surgical intervention works well</li></ul></li>
      </ul>
    </div>
    <div class="contact">
      <p class="contact__call">CALL US NOW : 555 014 2290</p>
      <p class="contact__line"><svg width="12" height="10" viewBox="0 0 12 10"><rect x=".6" y=".6" width="10.8" height="8.8" fill="none" stroke="#2e8a34" stroke-width="1.2"/><path d="M.6.8l5.4 4.4L11.4.8" fill="none" stroke="#2e8a34" stroke-width="1.2"/></svg>hello@wrenreferrals.com</p>
      <p class="contact__line"><svg width="12" height="12" viewBox="0 0 12 12"><circle cx="6" cy="6" r="5.3" fill="none" stroke="#2e8a34" stroke-width="1.2"/><path d="M.8 6h10.4M6 .8c-2.6 3-2.6 7.4 0 10.4M6 .8c2.6 3 2.6 7.4 0 10.4" fill="none" stroke="#2e8a34" stroke-width="1"/></svg>www.wrenreferrals.com</p>
    </div>
    <div class="affiliates" aria-label="Partner badges">
      <span></span><span></span><span></span><span></span><span></span><span></span>
    </div>
  </section>

</main>
</body>
</html>
```